Name card design for KOV mobile accessories company

KOV is an upmarket brand, we are looking for professional business card design.

the design should be neat and simple but giving a strong feeling.
should not be colorful. make it black/white/gray tone

Name:
Job title:
Contact no.:
company address: i would like the company address to be very small and thin.
link to social media profile:
company website:

*the company have no website yet
as the project is done please i also would like the font that use in design as well; for more further people in company need a business card:)
Updates

Thank you for all super fast submission :D they're all look cool!

i have just update my brief to make the statement clearer, please check it out :)
if you have any question please dont hesitate to ask.
i would like see more design from you! 
Keep it up!  :D

Target Market(s)

Company target are upmarket company distributor, such as Vordane and Pilto store.

Industry/Entity Type

Business

Font styles to use
Serif
Sans Serif
Other font styles liked:
• Formal and mordern

Colors
ffffff
eeeeee
d3d3d3
919191
474747
1b1b1b
000000
333333

Requirements
Must have
• The design must be professional clean and clear but also Strong and Modern!
text should be formal and mordern
Should not have
• No complicated design!

```html
<!DOCTYPE html>
<html lang="en">
<head>
<meta charset="utf-8">
<title>KOV Business Card</title>
<link rel="stylesheet" href="https://fonts.googleapis.com/css2?family=Lobster+Two:ital,wght@1,700&family=Lato:ital,wght@0,300;0,400;1,400&display=swap">
<style>
  :root {
    --white: #ffffff;
    --paper: #eeeeee;
    --light-gray: #d3d3d3;
    --mid-gray: #919191;
    --dark-gray: #474747;
    --charcoal: #333333;
    --ink: #1b1b1b;
    --black: #000000;
  }
  * { margin: 0; padding: 0; box-sizing: border-box; }
  html, body {
    width: 1200px;
    height: 750px;
    overflow: hidden;
    background: var(--light-gray);
    font-family: "Lato", sans-serif;
  }
  .stage {
    width: 1200px;
    height: 750px;
    display: flex;
    align-items: center;
    justify-content: center;
    gap: 40px;
  }
  .card {
    position: relative;
    width: 520px;
    height: 290px;
    border-radius: 26px;
    overflow: hidden;
  }
  .card-front {
    background: linear-gradient(160deg, var(--ink) 0%, var(--black) 100%);
    color: var(--white);
  }
  .card-back {
    background: var(--paper);
  }
  .identity {
    position: absolute;
    left: 44px;
    top: 118px;
  }
  .person-name {
    font-family: "Lobster Two", cursive;
    font-style: italic;
    font-weight: 700;
    font-size: 40px;
    line-height: 1;
    color: var(--white);
  }
  .person-title {
    font-family: "Lobster Two", cursive;
    font-style: italic;
    font-weight: 700;
    font-size: 14px;
    color: var(--white);
    text-align: right;
    margin-top: 4px;
  }
  .contact-list {
    position: absolute;
    left: 300px;
    top: 40px;
    list-style: none;
    border-left: 1px solid var(--dark-gray);
    padding-left: 14px;
  }
  .contact-item {
    display: flex;
    align-items: center;
    gap: 8px;
    font-size: 11px;
    font-weight: 400;
    line-height: 20px;
    color: var(--paper);
  }
  .contact-icon {
    width: 10px;
    height: 10px;
    flex: none;
  }
  .address {
    position: absolute;
    left: 44px;
    bottom: 34px;
    font-size: 8px;
    font-weight: 300;
    line-height: 12px;
    color: var(--dark-gray);
  }
  .brand-mark {
    position: absolute;
    right: 30px;
    bottom: 30px;
    font-family: "Lato", sans-serif;
    font-weight: 400;
    font-size: 26px;
    letter-spacing: 3px;
  }
  .card-front .brand-mark { color: var(--charcoal); bottom: 150px; }
  .card-back .brand-mark { color: var(--black); }
</style>
</head>
<body>
<main class="stage">
  <section class="card card-front" aria-label="Business card front">
    <div class="identity">
      <p class="person-name">Daniel Roswick</p>
      <p class="person-title">General Manager</p>
    </div>
    <ul class="contact-list">
      <li class="contact-item">
        <svg class="contact-icon" viewBox="0 0 10 10"><path d="M2 1 L4 1 L4.6 3 L3.5 4 Q4.5 6 6 6.5 L7 5.4 L9 6 L9 8 Q5 9 2 6 Q0.8 3.5 2 1 Z" fill="#eeeeee"/></svg>
        <span>555-014-2288</span>
      </li>
      <li class="contact-item">
        <svg class="contact-icon" viewBox="0 0 10 10"><rect x="0.5" y="2" width="9" height="6" fill="none" stroke="#eeeeee"/><path d="M0.5 2 L5 5.5 L9.5 2" fill="none" stroke="#eeeeee"/></svg>
        <span>daniel@kovmail.com</span>
      </li>
      <li class="contact-item">
        <svg class="contact-icon" viewBox="0 0 10 10"><rect x="1" y="1" width="8" height="8" fill="#eeeeee"/></svg>
        <span>www.socialnet.com/kov</span>
      </li>
      <li class="contact-item">
        <svg class="contact-icon" viewBox="0 0 10 10"><circle cx="5" cy="5" r="4" fill="#eeeeee"/></svg>
        <span>www.kov-mobile.com</span>
      </li>
    </ul>
    <address class="address">
      22 Cedar Row, Unit 5<br>
      Brookfield Hill<br>
      Eastmoor, KV<br>
      10208
    </address>
    <p class="brand-mark">KOV</p>
  </section>
  <section class="card card-back" aria-label="Business card back">
    <p class="brand-mark">KOV</p>
  </section>
</main>
</body>
</html>
```